Kitchen manufaturer business card/logo design

I am a small kitchen manufacturing company that makes and installs all sorts of cabinetry.

The colours im looking to incorporate in the card are light/baby blue, white and black.

Incorporate 5 stars to show quality workmanship and product.

Looking for a modern classy design.
Updates

Hey guys, New idea. The logo should be made using HK in the most modern way possible as well as the full company name below it. Thanks.

Target Market(s)

Anyone with a home thats looking for a new cabinetry of any sort.

Industry/Entity Type

Business

Contact Information for Business Card

Harbor Kitchens
Ted Lowther
PH 0491 358 902
Email- harborkitchens@mailvane.example
ABN- 83 507 962 318
-Kitchens
-Vanities
-Laundries
-Media Units
-Studies
-Wardrobes
-3D Computer Designs

Requirements
Must have

• The front of the card must only have the company name.
The different types of cabinetry I do must be on the back of the card in point form but instead of using points use stars.
Nice to have
• Just think classy and quality

```html
<!DOCTYPE html>
<html lang="en">
<head>
<meta charset="utf-8">
<title>Harbor Kitchens – Business Card</title>
<link rel="stylesheet" href="https://fonts.googleapis.com/css2?family=Questrial&family=Montserrat:wght@800&display=swap">
<style>
  :root {
    --backdrop: #2b2b2b;
    --card-dark: #1f1d1a;
    --card-light: #f7f7f7;
    --baby-blue: #29a9de;
    --ink: #4a4a4a;
    --ink-soft: #8a8a8a;
    --rule: #d4d4d4;
    --name-grey: #d9d9d9;
  }
  * { margin: 0; padding: 0; box-sizing: border-box; }
  html, body {
    width: 1200px;
    height: 900px;
    overflow: hidden;
    background: var(--backdrop);
  }
  .canvas {
    position: relative;
    width: 1200px;
    height: 900px;
    font-family: "Questrial", "Century Gothic", sans-serif;
  }
  .card {
    position: absolute;
    width: 600px;
    height: 343px;
    border-radius: 3px;
    box-shadow: 0 18px 40px rgba(0,0,0,0.45);
  }

  /* Front */
  .card-front {
    left: 90px;
    top: 90px;
    background: var(--card-dark);
    display: flex;
    flex-direction: column;
    align-items: center;
    justify-content: center;
    gap: 26px;
  }
  .brand-square {
    width: 64px;
    height: 64px;
    background: var(--baby-blue);
  }
  .brand-name {
    color: var(--name-grey);
    font-size: 34px;
    letter-spacing: 1px;
    text-transform: uppercase;
  }

  /* Back */
  .card-back {
    left: 510px;
    top: 470px;
    background: var(--card-light);
    color: var(--ink);
  }
  .divider {
    position: absolute;
    left: 0;
    right: 0;
    top: 132px;
    height: 2px;
    background: var(--rule);
  }
  .services {
    position: absolute;
    right: 28px;
    font-size: 19px;
    text-transform: uppercase;
    letter-spacing: 0.5px;
    white-space: nowrap;
  }
  .services-top { top: 96px; }
  .services-bottom { top: 146px; }
  .star { color: var(--baby-blue); font-size: 12px; vertical-align: 3px; padding: 0 5px; }
  .faint-mark {
    position: absolute;
    left: 70px;
    top: 104px;
    width: 58px;
    height: 58px;
    background: #ececec;
  }
  .abn {
    position: absolute;
    right: 28px;
    top: 232px;
    font-size: 13px;
    color: var(--ink-soft);
    letter-spacing: 0.5px;
  }
  .contact {
    position: absolute;
    left: 30px;
    bottom: 30px;
  }
  .contact-name {
    font-family: "Montserrat", "Arial Black", sans-serif;
    font-weight: 800;
    font-size: 19px;
    text-transform: uppercase;
    color: var(--ink);
    margin-bottom: 10px;
  }
  .contact-line {
    font-size: 16px;
    color: var(--ink-soft);
  }
  .label { color: var(--baby-blue); font-weight: bold; }
</style>
</head>
<body>
<main class="canvas">
  <section class="card card-front">
    <div class="brand-square"></div>
    <h1 class="brand-name">Harbor Kitchens</h1>
  </section>

  <section class="card card-back">
    <div class="faint-mark"></div>
    <div class="divider"></div>
    <p class="services services-top">Kitchens<span class="star">★</span>Vanities<span class="star">★</span>Laundries<span class="star">★</span>Media Units</p>
    <p class="services services-bottom">Studies<span class="star">★</span>Wardrobes<span class="star">★</span>3D Computer Designs</p>
    <p class="abn">ABN: 83 507 962 318</p>
    <div class="contact">
      <p class="contact-name">Ted Lowther</p>
      <p class="contact-line"><span class="label">T:</span> 0491 358 902 · <span class="label">E:</span> harborkitchens@mailvane.example</p>
    </div>
  </section>
</main>
</body>
</html>
```